Pelorin Conference

We need a pullup banner 23x63 inches. We are attaching an example of a draft that we created. Can you please make it look more professional?
Thank you!

```html
<!DOCTYPE html>
<html lang="en">
<head>
<meta charset="utf-8">
<title>Halvard Climate – Pull-up Banners</title>
<link rel="stylesheet" href="https://fonts.googleapis.com/css2?family=Bebas+Neue&family=Montserrat:wght@500;600;800&display=swap">
<style>
  :root {
    --stage: #d6d6d6;
    --navy: #0e1655;
    --navy-deep: #0a0f3f;
    --orange: #e2700f;
    --white: #ffffff;
    --paper: #f1f2f4;
    --sky-top: #1f5fb8;
    --sky-mid: #5fa6e6;
    --sky-low: #cfe3f5;
  }
  * { margin: 0; padding: 0; box-sizing: border-box; }
  html, body { width: 1200px; height: 1181px; overflow: hidden; }
  body {
    background: var(--stage);
    font-family: "Montserrat", sans-serif;
    position: relative;
  }
  .banner {
    position: absolute;
    top: 200px;
    width: 300px;
    height: 769px;
    background: var(--navy);
    overflow: hidden;
  }
  .banner--headline { left: 250px; }
  .banner--services { left: 650px; }

  .banner__top {
    position: absolute; inset: 0 0 auto 0;
    width: 300px; height: 400px;
  }
  .brand {
    position: absolute; top: 50px; left: 0; right: 0;
    display: flex; align-items: center; justify-content: center; gap: 12px;
  }
  .brand__dot {
    width: 40px; height: 40px; border-radius: 50%;
    background: var(--orange);
  }
  .brand__name {
    font-weight: 800; font-size: 17px; line-height: 1.1;
    color: var(--navy); letter-spacing: 0.5px; text-transform: uppercase;
  }

  .headline {
    position: absolute; top: 410px; left: 0; right: 0;
    text-align: center; color: var(--white);
    font-family: "Bebas Neue", sans-serif;
    font-size: 40px; line-height: 38px; letter-spacing: 0.3px;
  }
  .cta {
    position: absolute; left: 40px; width: 220px; height: 30px;
    border-radius: 15px; background: var(--orange);
    color: var(--white); font-weight: 800; font-size: 17px;
    display: flex; align-items: center; justify-content: center;
    letter-spacing: 0.5px; text-transform: uppercase;
  }
  .banner--headline .cta { top: 655px; }
  .banner--services .cta { top: 640px; }

  .contact {
    position: absolute; left: 0; right: 0;
    color: var(--white); font-size: 11px; font-weight: 500;
    text-align: center; line-height: 17px;
  }
  .banner--headline .contact { top: 700px; }
  .banner--services .contact { top: 685px; }
  .contact__line { display: flex; align-items: center; justify-content: center; gap: 6px; }
  .contact__line svg { width: 10px; height: 10px; }

  .services {
    position: absolute; top: 430px; left: 0; right: 0;
    display: flex; flex-direction: column; gap: 32px;
  }
  .services__row { display: flex; justify-content: center; }
  .service {
    width: 90px; display: flex; flex-direction: column; align-items: center; gap: 10px;
    color: var(--white); font-size: 10px; font-weight: 600; text-transform: uppercase;
    position: relative;
  }
  .service + .service::before {
    content: ""; position: absolute; left: 0; top: 0; height: 72px;
    border-left: 1.5px dashed var(--white);
  }
  .service svg { width: 42px; height: 42px; }
</style>
</head>
<body>

<svg width="0" height="0" style="position:absolute">
  <defs>
    <linearGradient id="sky" x1="0" y1="0" x2="0.3" y2="1">
      <stop offset="0" stop-color="#1f5fb8"/>
      <stop offset="0.55" stop-color="#5fa6e6"/>
      <stop offset="1" stop-color="#cfe3f5"/>
    </linearGradient>
    <linearGradient id="paper" x1="0" y1="0" x2="1" y2="1">
      <stop offset="0" stop-color="#e9eaed"/>
      <stop offset="1" stop-color="#fbfbfc"/>
    </linearGradient>
    <symbol id="banner-top" viewBox="0 0 300 400">
      <rect width="300" height="400" fill="url(#paper)"/>
      <path d="M0 175 Q150 65 300 112 L300 400 L0 400 Z" fill="#0e1655"/>
      <path d="M0 200 Q150 95 300 132 L300 152 Q150 118 0 218 Z" fill="#e2700f"/>
      <path d="M0 222 Q150 124 300 158 L300 328 Q150 400 0 342 Z" fill="#ffffff"/>
      <path d="M0 226 Q150 128 300 162 L300 324 Q150 394 0 338 Z" fill="url(#sky)" role="img" aria-label="Photo of wind turbines and solar panels under a blue sky"/>
      <path d="M0 346 Q150 404 300 332 L300 346 Q150 428 0 378 Z" fill="#e2700f"/>
    </symbol>
    <symbol id="tick-badge" viewBox="0 0 42 42">
      <circle cx="21" cy="21" r="19" fill="#ffffff" stroke="#0e1655" stroke-width="2"/>
      <path d="M4 25 A17 17 0 0 0 38 25 Z" fill="#e2700f"/>
      <circle cx="21" cy="19" r="12" fill="#ffffff"/>
      <path d="M15 19 L19.5 23.5 L27 15" fill="none" stroke="#e2700f" stroke-width="3" stroke-linecap="round" stroke-linejoin="round"/>
    </symbol>
    <symbol id="icon-mail" viewBox="0 0 10 10">
      <rect x="0.5" y="1.5" width="9" height="7" fill="none" stroke="#e2700f"/>
      <path d="M0.5 1.5 L5 5.5 L9.5 1.5" fill="none" stroke="#e2700f"/>
    </symbol>
    <symbol id="icon-web" viewBox="0 0 10 10">
      <circle cx="5" cy="5" r="4.3" fill="none" stroke="#e2700f"/>
      <ellipse cx="5" cy="5" rx="2" ry="4.3" fill="none" stroke="#e2700f"/>
      <path d="M0.7 5 H9.3" stroke="#e2700f"/>
    </symbol>
  </defs>
</svg>

<section class="banner banner--headline">
  <svg class="banner__top"><use href="#banner-top"/></svg>
  <div class="brand">
    <span class="brand__dot"></span>
    <span class="brand__name">Halvard<br>Climate</span>
  </div>
  <h1 class="headline">Scaling<br>the market for<br>weather, climate<br>and natural<br>catastrophe<br>risk transfer.</h1>
  <div class="cta">Contact us</div>
  <div class="contact">
    <p class="contact__line"><svg><use href="#icon-mail"/></svg>contact@halvardclimate.com</p>
    <p class="contact__line"><svg><use href="#icon-web"/></svg>www.halvardclimate.com</p>
  </div>
</section>

<section class="banner banner--services">
  <svg class="banner__top"><use href="#banner-top"/></svg>
  <div class="brand">
    <span class="brand__dot"></span>
    <span class="brand__name">Halvard<br>Climate</span>
  </div>
  <div class="services">
    <div class="services__row">
      <div class="service"><svg><use href="#tick-badge"/></svg>Advisory</div>
      <div class="service"><svg><use href="#tick-badge"/></svg>Structuring</div>
      <div class="service"><svg><use href="#tick-badge"/></svg>Placement</div>
    </div>
    <div class="services__row">
      <div class="service"><svg><use href="#tick-badge"/></svg>Underwriting</div>
      <div class="service"><svg><use href="#tick-badge"/></svg>Analytics</div>
    </div>
  </div>
  <div class="cta">Contact us</div>
  <div class="contact">
    <p class="contact__line"><svg><use href="#icon-mail"/></svg>contact@halvardclimate.com</p>
    <p class="contact__line"><svg><use href="#icon-web"/></svg>www.halvardclimate.com</p>
  </div>
</section>

</body>
</html>
```